Halvorn spray foam and Environmental

I have business cards but need new ones. The ones I have are very bland. Here is. Y company website http://www.halvornsprayfoam.ca

Also I can send you copies of the current cards
I would also need my current logo on the new design as well.. Also spray foam and Environmental

Industry/Entity Type

Business

Logo Text

Halvorn.

```html
<!DOCTYPE html>
<html lang="en">
<head>
<meta charset="utf-8">
<title>Halvorn Business Cards</title>
<link href="https://fonts.googleapis.com/css2?family=Montserrat:wght@800&family=Oswald:wght@600&family=Open+Sans:wght@400&family=EB+Garamond:wght@400&display=swap" rel="stylesheet">
<style>
  :root {
    --bg: #e4e4e6;
    --card: #ffffff;
    --purple: #5f3a8c;
    --green: #3dbb1f;
    --grey-text: #8a8a8a;
    --ink: #2b2b2b;
    --rule: #c9c9c9;
    --mark-grey: #6e6a6c;
  }
  * { box-sizing: border-box; margin: 0; padding: 0; }
  html, body { width: 1200px; height: 904px; overflow: hidden; }
  body {
    background: var(--bg);
    display: flex;
    flex-direction: column;
    align-items: center;
    justify-content: center;
    gap: 40px;
  }
  .card {
    width: 680px;
    height: 389px;
    background: var(--card);
    border-radius: 18px;
    box-shadow: 0 6px 18px rgba(0,0,0,0.18);
    position: relative;
  }
  /* Front */
  .card-front {
    display: flex;
    flex-direction: column;
    align-items: center;
    justify-content: center;
    gap: 34px;
  }
  .lockup { display: flex; flex-direction: column; align-items: center; position: relative; width: 100%; }
  .lockup::before, .lockup::after {
    content: ""; position: absolute; left: 130px; right: 130px; height: 1px; background: var(--rule);
  }
  .lockup::before { top: -16px; }
  .lockup::after { bottom: -16px; }
  .brand-row { display: flex; align-items: center; gap: 12px; }
  .brand-square { width: 44px; height: 36px; border-radius: 6px; background: var(--mark-grey); }
  .brand-name {
    font-family: "Montserrat", sans-serif; font-weight: 800; font-size: 26px;
    color: var(--purple); line-height: 1.05; text-transform: uppercase;
  }
  .tagline { font-family: "EB Garamond", serif; font-size: 24px; margin-top: 4px; }
  .tagline-green { color: var(--green); }
  .tagline-grey { color: var(--grey-text); }
  /* Back */
  .card-back { display: flex; align-items: center; }
  .back-brand {
    width: 50%; display: flex; flex-direction: column; align-items: center; gap: 14px;
  }
  .back-square { width: 190px; height: 130px; border-radius: 18px; background: var(--mark-grey); }
  .back-name {
    font-family: "Montserrat", sans-serif; font-weight: 800; font-size: 24px;
    color: var(--purple); text-transform: uppercase;
  }
  .divider { width: 1px; height: 110px; background: var(--ink); }
  .contact { padding-left: 70px; }
  .person-name {
    font-family: "Oswald", sans-serif; font-weight: 600; font-size: 36px;
    color: var(--purple); text-transform: uppercase; line-height: 1;
  }
  .person-role { font-family: "Open Sans", sans-serif; font-size: 15px; color: var(--ink); margin: 4px 0 8px; }
  .contact-list { list-style: none; font-family: "Open Sans", sans-serif; font-size: 15px; color: var(--ink); }
  .contact-list li { display: flex; align-items: center; gap: 10px; margin-bottom: 4px; }
  .contact-list svg { width: 15px; height: 15px; flex: none; }
</style>
</head>
<body>
  <section class="card card-front">
    <div class="lockup">
      <div class="brand-row">
        <span class="brand-square"></span>
        <span class="brand-name">Halvorn Environmental</span>
      </div>
      <p class="tagline tagline-green">Residential &amp; Commercial</p>
    </div>
    <div class="lockup">
      <div class="brand-row">
        <span class="brand-square"></span>
        <span class="brand-name">Halvorn Spray Foam Ltd.</span>
      </div>
      <p class="tagline tagline-grey">Residential &amp; Commercial</p>
    </div>
  </section>

  <section class="card card-back">
    <div class="back-brand">
      <span class="back-square"></span>
      <span class="back-name">Halvorn</span>
    </div>
    <span class="divider"></span>
    <div class="contact">
      <h1 class="person-name">Ryan Calder</h1>
      <p class="person-role">Manager</p>
      <ul class="contact-list">
        <li>
          <svg viewBox="0 0 16 16"><circle cx="8" cy="8" r="8" fill="#5f3a8c"/><path d="M5 4.5c.5-.5 1.2-.3 1.4.3l.4 1.1c.1.4 0 .7-.3.9l-.4.3c.4.9 1.1 1.6 2 2l.3-.4c.2-.3.6-.4.9-.3l1.1.4c.6.2.8.9.3 1.4-.8.8-2 .9-3.3.1A8 8 0 0 1 4.9 7.8C4.1 6.5 4.2 5.3 5 4.5z" fill="#fff"/></svg>
          +1 555 014 2290
        </li>
        <li>
          <svg viewBox="0 0 16 16"><circle cx="8" cy="8" r="8" fill="#5f3a8c"/><rect x="4" y="5" width="8" height="6" rx="1" fill="#fff"/><path d="M4.3 5.4 8 8.3l3.7-2.9" stroke="#5f3a8c" stroke-width="0.9" fill="none"/></svg>
          info@halvornsprayfoam.ca
        </li>
        <li>
          <svg viewBox="0 0 16 16"><circle cx="8" cy="8" r="8" fill="#5f3a8c"/><g stroke="#fff" stroke-width="0.9" fill="none"><circle cx="8" cy="8" r="4"/><ellipse cx="8" cy="8" rx="1.8" ry="4"/><path d="M4 8h8"/></g></svg>
          www.halvornsprayfoam.ca
        </li>
      </ul>
    </div>
  </section>
</body>
</html>
```